Book Cover for Fitness Trainer for Men

My name is Mabel Joy Crane. I am a female Fitness Trainer for Men.
I need a new Book Cover Design for my second book and a back of the book.
Both with updated text.
#A… Book Cover… I like the bright red and yellow colors.
I like the weight rack and the bold headline Font
#B… Book Cover…I like the full frontal sexier body. I don not like the font style.
I want the new design sexier; super sexy. Even more eye catching for guys.
I want to push the envelope to the point of almost too much sexy.
An Brindlo book 6”x9”, 150 pages

Target Market(s)

Men

Industry/Entity Type

Health and fitness for men

Colors
FFF300
FFF600
FEFA6F
FFFEC7
FFFEE8
EB3D1F
EC4F4E
F09395
F8D3D4
FCEDEE

Requirements
Must have
• Sexy & eye catching.

```html
<!DOCTYPE html>
<html lang="en">
<head>
<meta charset="utf-8">
<title>Fitness Trainer for Men – Book Cover Spread</title>
<link rel="stylesheet" href="https://fonts.googleapis.com/css2?family=Anton&family=Arimo:wght@400;700&family=Barlow:wght@400;500;700;800&family=Oswald:wght@400;500&display=swap">
<style>
  :root {
    --stage: #f0c6e2;
    --back: #ef9190;
    --front: #fcedee;
    --blush: #f8d3d4;
    --rose: #f09395;
    --red: #ec4f4e;
    --red-deep: #eb3d1f;
    --ink: #141414;
    --skin-a: #d9a47e;
    --skin-b: #9c6a4c;
  }
  * { margin: 0; padding: 0; box-sizing: border-box; }
  html, body { width: 1200px; height: 2561px; overflow: hidden; }
  body { background: var(--stage); position: relative; font-family: "Arimo", Arial, sans-serif; color: var(--ink); }

  .spread { position: absolute; left: 0; top: 885px; width: 1200px; height: 815px; }

  /* Back cover */
  .back-cover { position: absolute; left: 0; top: 0; width: 620px; height: 815px; background: var(--back); }
  .blurb { position: absolute; left: 0; width: 590px; text-align: center; font-size: 12px; line-height: 13.7px; }
  .blurb b { font-weight: 700; }
  .blurb-heading { font-size: 15px; font-weight: 500; line-height: 18px; }
  .blurb-mission { font-size: 13.5px; line-height: 15px; font-weight: 700; }
  .blurb-mission span { font-size: 12px; }
  .author-photo-frame { position: absolute; left: 238px; top: 577px; width: 104px; height: 112px; background: var(--red); transform: rotate(-4deg); }
  .author-photo { position: absolute; left: 243px; top: 573px; width: 100px; height: 114px; background: linear-gradient(160deg, #efe3d8, #c89a78 55%, #3f6b6a); }
  .author-caption { position: absolute; left: 0; width: 590px; text-align: center; font-size: 12px; line-height: 14px; }
  .spine-title { position: absolute; left: 590px; top: 185px; writing-mode: vertical-rl; font-family: "Barlow", sans-serif; font-size: 19px; letter-spacing: 9.6px; color: var(--red); }

  /* Front cover */
  .front-cover { position: absolute; left: 620px; top: 0; width: 580px; height: 815px; background: var(--front); overflow: hidden; }
  .front-shapes { position: absolute; inset: 0; }
  .model-photo { position: absolute; left: 262px; top: 160px; width: 300px; height: 655px; background: linear-gradient(180deg, var(--skin-a), var(--skin-b) 45%, #8b8b8b 75%, var(--skin-a)); border-radius: 130px 130px 20px 20px; }
  .title { position: absolute; left: 165px; top: 10px; font-family: "Anton", sans-serif; font-weight: 400; font-size: 96px; line-height: 100px; letter-spacing: 19px; color: var(--red); white-space: nowrap; }
  .subtitle { position: absolute; left: 166px; top: 117px; font-family: "Barlow", sans-serif; font-weight: 500; font-size: 20px; letter-spacing: 6.4px; color: var(--red); }
  .author-name { position: absolute; left: 30px; top: 198px; font-family: "Barlow", sans-serif; font-weight: 800; font-size: 63px; line-height: 65px; letter-spacing: 1.5px; color: var(--red); }
  .promise { position: absolute; left: 31px; font-family: "Barlow", sans-serif; font-weight: 500; font-size: 19px; line-height: 25px; letter-spacing: 0.8px; color: var(--ink); }
  .stories { position: absolute; left: 20px; top: 690px; width: 165px; text-align: center; font-family: "Oswald", sans-serif; font-size: 18px; line-height: 23px; color: var(--ink); }
  .stories .lead { color: var(--red); }
</style>
</head>
<body>
  <main class="spread">
    <section class="back-cover">
      <p class="blurb" style="top:56px">I've been using eye candy to get guys interested in health and<br>fitness since the day I walked in the gym and turned heads.&nbsp; I figured if<br>you wanted Tits &amp; Ass I'd give it to you.&nbsp; Enough to make a buck and get<br>my guys healthier. As a personal fitness trainer for Men I've learned…that<br>not all Guys are the same.&nbsp; Each of you is different and You need to find<br>what works for You.&nbsp; When you do … the the pounds melt away, your gut<br>shrinks, and your health improves.</p>
      <p class="blurb" style="top:164px">You'll love the new you.&nbsp; Your girl friend will love it. Your wife will love it.<br>Nothing a woman loves more than a long rock hard man in shape.</p>
      <p class="blurb" style="top:206px">While everybody in the fitness community screams and yells about<br>gym memberships, 30 day challenges, and complete diet changes …<br>My Guys don't do all that.&nbsp; My Guys are Real Men with Real bodies.<br>Real Men that work for a living and don't have time to live in the gym.</p>
      <p class="blurb" style="top:273px">Real men are tired of gym rats with "Look at me" egos, God given<br>1% body fat and abs you'll never get.&nbsp; These guys are full of Shit!&nbsp; And<br>they're the first one to buy my book.&nbsp; Ya gotta love it.</p>
      <p class="blurb blurb-heading" style="top:326px">You need to find what works for you.</p>
      <p class="blurb" style="top:346px">"I made a few adjustment in my meals added a minimum amount of exercise and<br>lost 17 pounds in three months.&nbsp; Thanks Mabel. Couldn't have done it without you."</p>
      <p class="blurb" style="top:386px"><b>"Mabel I took your bait</b> and it actually made sense. Can't believe you got me exercising.<br>My gut shrunk and had to buy new pants.&nbsp; Best 20 bucks I ever spent."<br><b>"I've tried a few expensive</b> 30day programs but your <b>Ultimate Workout</b> was all<br>I ever needed.&nbsp; You're right <b>No F**king secret here."</b>&nbsp; <b>"Strategically eating Fast food</b> is genius.<br>Never thought I could still eat "the good stuff" and lose weight. WOW!"<br><b>"My increasing weight</b> was scaring the hell out of me.&nbsp; Showing me that it's the<br>little changes I can do…that has changed everything." <b>"Everybody wanted me to make big</b><br>drastic changes in my life. I can't do that.&nbsp; All these little "Tricks of the Trade" I can do.<br>" Thank you Mabel."</p>
      <p class="blurb blurb-mission" style="top:511px">Real Men can be fit, healthy and in shape no matter their size, weight, or body fat.<br><span>My mission is to get your lazy ass in shape by finding what works for you.<br>If I need to get your attention first…Then that's what I'll do.</span></p>
      <div class="author-photo-frame"></div>
      <div class="author-photo" role="img" aria-label="Portrait photo of the author"></div>
      <p class="author-caption" style="top:703px">Mabel Joy Crane<br>Fitness Trainer for Men</p>
      <p class="author-caption" style="top:744px">Think you can do Twenty bucks to Get You Hot, Sweaty, and Hard?</p>
      <div class="spine-title">FITNESS TRAINER FOR MEN</div>
    </section>

    <section class="front-cover">
      <svg class="front-shapes" width="580" height="815" viewBox="0 0 580 815">
        <polygon points="0,0 170,0 0,150" fill="var(--rose)"/>
        <polygon points="0,150 170,75 0,260" fill="var(--blush)" opacity="0.6"/>
        <polygon points="0,815 0,660 340,600 400,815" fill="var(--blush)"/>
        <polygon points="400,210 580,110 580,480" fill="var(--red)"/>
        <polygon points="420,300 580,170 580,815 300,815" fill="var(--rose)"/>
        <polygon points="190,645 370,470 330,815" fill="var(--red)"/>
        <polygon points="500,150 560,120 520,200" fill="var(--blush)"/>
      </svg>
      <div class="model-photo" role="img" aria-label="Photo of a fit woman in a grey sports bra and shorts, arms raised behind her head"></div>
      <h1 class="title">FITNESS</h1>
      <p class="subtitle">TRAINER FOR MEN</p>
      <h2 class="author-name">MABEL<br>JOY<br>CRANE</h2>
      <p class="promise" style="top:452px">HELPING GUYS GET<br>HOT, SWEATY, &amp; HARD</p>
      <p class="promise" style="top:509px">SO POUNDS MELT AWAY,<br>YOUR GUT SHRINKS,<br>&amp; YOU LAST LONGER.</p>
      <p class="stories"><span class="lead">DOZEN OF SUCCESS</span><br>STORIES FROM<br>REAL GUYS<br>WITH REAL RESULTS</p>
    </section>
  </main>
</body>
</html>
```